2019 CD Cover Design - Drifting Past Noon

Please Use Uploaded Photo. Feel free to crop and otherwise edit the photo to enrich the design. Title is "Drifting Past Noon" and should be relative prominent in the cover. Artist names are "Marcus Pellham and Rosalind Quaye" and should also be printed on the cover. Please ensure compliance with DiscHarbor Published Requirements, ie CMYK, 300dpi, etc. Planning on giving winner the Back Cover and Inside designs.

Target Market(s)

The album is a set of cover love songs, all duets, many are contemporary country, ie in the style of Copper Wagonwheel, Greta Voss, Harlow Junction. Feel free to innovate!

Industry/Entity Type

Music Download

Colors

Designer to choose colors to be used in the design.

Requirements
Nice to have
• Optional - Third Line of Text - “Contemporary Country Duets”
Should not have
• Please do NOT cut out and completely replace the grassy field background. The CD liner notes will discuss the photo, which is a renowned national park in our hometown.

```html
<!DOCTYPE html>
<html lang="en">
<head>
<meta charset="utf-8">
<title>Drifting Past Noon — Album Cover</title>
<link href="https://fonts.googleapis.com/css2?family=Yellowtail&family=Open+Sans:wght@600;700&display=swap" rel="stylesheet">
<style>
  :root {
    --field-gold: #d9a94a;
    --field-light: #e8c778;
    --field-green: #9bb04a;
    --shirt-grey: #55585e;
    --dress-black: #1c1a1c;
    --label-amber: #e2a247;
    --label-ink: #2b1d08;
    --white: #ffffff;
  }
  html, body {
    margin: 0;
    padding: 0;
    overflow: hidden;
    background: #ffffff;
  }
  .cover {
    position: relative;
    width: 1200px;
    height: 1200px;
    overflow: hidden;
  }
  .cover-photo {
    position: absolute;
    inset: 0;
    background:
      radial-gradient(ellipse 30% 55% at 25% 75%, var(--shirt-grey) 0%, rgba(85,88,94,0.85) 55%, rgba(85,88,94,0) 100%),
      radial-gradient(ellipse 35% 55% at 78% 85%, var(--dress-black) 0%, rgba(28,26,28,0.8) 55%, rgba(28,26,28,0) 100%),
      radial-gradient(ellipse 40% 40% at 95% 40%, var(--field-green) 0%, rgba(155,176,74,0) 100%),
      linear-gradient(180deg, var(--field-light) 0%, var(--field-gold) 55%, #b98a3a 100%);
  }
  .album-title {
    position: absolute;
    left: 250px;
    top: 640px;
    width: 500px;
    margin: 0;
    font-family: "Yellowtail", cursive;
    font-weight: 400;
    color: var(--white);
    line-height: 0.82;
    text-align: center;
  }
  .album-title .line-1 { display: block; font-size: 150px; }
  .album-title .line-2 { display: block; font-size: 90px; margin: 6px 0 0 60px; }
  .album-title .line-3 { display: block; font-size: 170px; margin-left: -40px; }
  .artist-label {
    position: absolute;
    left: 602px;
    top: 1020px;
    width: 338px;
    height: 70px;
    box-sizing: border-box;
    padding: 6px 12px 0 14px;
    background: var(--label-amber);
    font-family: "Open Sans", sans-serif;
    font-weight: 700;
    font-size: 22px;
    line-height: 28px;
    color: var(--label-ink);
    text-transform: uppercase;
    letter-spacing: 0.2px;
  }
  .tagline {
    position: absolute;
    left: 410px;
    top: 1110px;
    width: 412px;
    margin: 0;
    font-family: "Open Sans", sans-serif;
    font-weight: 600;
    font-size: 20px;
    letter-spacing: 4px;
    color: var(--white);
    text-align: center;
    text-transform: uppercase;
    white-space: nowrap;
  }
</style>
</head>
<body>
  <main class="cover">
    <div class="cover-photo" role="img" aria-label="Photo of the duo, a white-haired man in a grey t-shirt and a woman with long wavy blonde hair in black lace, kneeling in a golden grassy field in the national park"></div>
    <h1 class="album-title">
      <span class="line-1">Drifting</span>
      <span class="line-2">Past</span>
      <span class="line-3">Noon</span>
    </h1>
    <div class="artist-label">Marcus Pellham and<br>Rosalind Quaye</div>
    <p class="tagline">Contemporary Country Duets</p>
  </main>
</body>
</html>
```